TernQuay Business Cards

Create business cards for our exciting new software company. We provide cloud billing systems and provisioning software for campany that need monthly SaaS and Cloud Billing

Target Market(s)

Enterprise businesses, b2b, telecom carriers, software manufactures

Industry/Entity Type

Software

```html
<!DOCTYPE html>
<html lang="en">
<head>
<meta charset="utf-8">
<title>TernQuay Business Cards</title>
<link href="https://fonts.googleapis.com/css2?family=Rubik:ital,wght@0,400;0,500;0,700;1,400&display=swap" rel="stylesheet">
<style>
  :root {
    --stage: #d9dcdf;
    --paper: #eceef0;
    --paper-shade: #d8dde2;
    --navy: #17304f;
    --navy-deep: #132845;
    --steel: #2f4c6b;
    --sky: #6cb4d4;
    --sky-soft: #5a9dc0;
    --white: #ffffff;
    --ink-soft: #4a5866;
  }
  * { box-sizing: border-box; margin: 0; padding: 0; }
  html, body { width: 1200px; height: 880px; overflow: hidden; }
  body {
    background: var(--stage);
    font-family: "Rubik", Arial, sans-serif;
    display: flex;
    align-items: center;
    justify-content: center;
    gap: 40px;
  }
  .card {
    position: relative;
    width: 540px;
    height: 310px;
    border-radius: 4px;
    overflow: hidden;
    box-shadow: 0 10px 24px rgba(0,0,0,.18);
  }

  /* front */
  .card--front { background: linear-gradient(160deg, var(--white), var(--paper) 45%, var(--paper-shade)); }
  .card__panel { position: absolute; inset: 0; }
  .brand { position: absolute; top: 34px; left: 38px; }
  .brand__row { display: flex; align-items: center; gap: 10px; }
  .brand__dot { width: 14px; height: 14px; border-radius: 50%; background: var(--steel); }
  .brand__name { font-size: 36px; font-weight: 500; color: var(--steel); letter-spacing: .5px; line-height: 1; }
  .brand__tagline {
    margin-top: 8px;
    font-size: 7.5px;
    letter-spacing: 1.4px;
    text-transform: uppercase;
    color: var(--ink-soft);
    text-align: right;
    line-height: 1.35;
  }
  .person { position: absolute; right: 40px; top: 128px; text-align: right; color: var(--white); }
  .person__name { font-size: 19px; font-weight: 700; }
  .person__role { font-size: 13px; font-style: italic; margin-top: 2px; }
  .contacts { position: absolute; right: 30px; top: 186px; color: var(--white); list-style: none; }
  .contacts li {
    display: flex; justify-content: flex-end; align-items: center; gap: 12px;
    font-size: 14.5px; line-height: 21px;
  }
  .contacts li.address { margin-top: 12px; font-size: 14px; }
  .contacts svg { width: 14px; height: 14px; flex: none; }

  /* back */
  .card--back { background: radial-gradient(circle at 40% 30%, var(--navy), var(--navy-deep)); }
  .card__arc { position: absolute; inset: 0; }
  .brand--back { top: auto; left: auto; right: 36px; top: 104px; }
  .brand--back .brand__name { color: var(--sky); font-size: 40px; }
  .brand--back .brand__dot { background: var(--sky); }
  .brand--back .brand__tagline { color: #cfe3ee; font-size: 8px; }
</style>
</head>
<body>

  <section class="card card--front" aria-label="Business card front">
    <svg class="card__panel" viewBox="0 0 540 310" aria-hidden="true">
      <defs>
        <linearGradient id="panelFill" x1="0" y1="1" x2="1" y2="0">
          <stop offset="0" stop-color="#5ea3c4"/>
          <stop offset=".55" stop-color="#2e5677"/>
          <stop offset="1" stop-color="#1d3756"/>
        </linearGradient>
      </defs>
      <path d="M70 310 C90 200 200 130 340 118 C440 110 510 130 540 150 L540 310 Z" fill="url(#panelFill)"/>
    </svg>

    <div class="brand">
      <div class="brand__row">
        <span class="brand__dot"></span>
        <span class="brand__name">TernQuay</span>
      </div>
      <p class="brand__tagline">Cloud billing and<br>operational support systems</p>
    </div>

    <div class="person">
      <p class="person__name">Name Surname</p>
      <p class="person__role">manager</p>
    </div>

    <ul class="contacts">
      <li>+00 123 456 789
        <svg viewBox="0 0 14 14"><rect x="4" y="1" width="6" height="12" rx="1" fill="none" stroke="#fff" stroke-width="1.3"/><line x1="6" y1="11" x2="8" y2="11" stroke="#fff"/></svg>
      </li>
      <li>name.surname@domain.com
        <svg viewBox="0 0 14 14"><rect x="1" y="3" width="12" height="8" fill="none" stroke="#fff" stroke-width="1.2"/><path d="M1 3 L7 8 L13 3" fill="none" stroke="#fff" stroke-width="1.2"/></svg>
      </li>
      <li>www.domain.com
        <svg viewBox="0 0 14 14"><circle cx="7" cy="7" r="5.5" fill="none" stroke="#fff" stroke-width="1.1"/><ellipse cx="7" cy="7" rx="2.3" ry="5.5" fill="none" stroke="#fff" stroke-width="1"/><line x1="1.5" y1="7" x2="12.5" y2="7" stroke="#fff"/></svg>
      </li>
      <li class="address">Your Address Goes Here, City, Country, Zipcode
        <svg viewBox="0 0 14 14"><path d="M1 7 L7 1.5 L13 7 L11 7 L11 13 L8.5 13 L8.5 9 L5.5 9 L5.5 13 L3 13 L3 7 Z" fill="#fff"/></svg>
      </li>
    </ul>
  </section>

  <section class="card card--back" aria-label="Business card back">
    <svg class="card__arc" viewBox="0 0 540 310" aria-hidden="true">
      <defs>
        <linearGradient id="arcStroke" x1="0" y1="0" x2="1" y2="1">
          <stop offset="0" stop-color="#3b5e80" stop-opacity=".6"/>
          <stop offset="1" stop-color="#6cb4d4"/>
        </linearGradient>
      </defs>
      <path d="M-10 110 C40 60 140 40 210 70 C280 100 300 200 280 320" fill="none" stroke="url(#arcStroke)" stroke-width="8"/>
    </svg>

    <div class="brand brand--back">
      <div class="brand__row">
        <span class="brand__dot"></span>
        <span class="brand__name">TernQuay</span>
      </div>
      <p class="brand__tagline">Cloud billing and<br>operational support systems</p>
    </div>
  </section>

</body>
</html>
```